Small but growing painting company. Have built up a steady client base. Want to start having a more professional look. Want to start with changing my business cards, and also getting new logo and tee shirts.

Target Market(s)

Home owners, property management companies, all ages 30-70

Industry/Entity Type

Painting And Decorating

Contact Information for Business Card

Bright Ridge Painting LLC Mark Delvecchi 630-584-3907 interior, exterior, vaulted ceiling, drywall repair, pressure washing, kitchen cabinets, epoxy, garage floors,

Font styles to use
Sans Serif
Other font styles liked:
• Harrington

Colors
0355a3
ffffff
ec1f27
000000
3176b5
0493ce
474747
b7b7b7

Requirements
Must have
• Creative, something that doesn’t look like every other painting card.
Nice to have
• I would like something with an arrow or something going to a point

```html
<!DOCTYPE html>
<html lang="en">
<head>
<meta charset="utf-8">
<title>Bright Ridge Painting LLC – Business Card</title>
<link rel="stylesheet" href="https://fonts.googleapis.com/css2?family=Roboto:wght@400;700&display=swap">
<style>
  :root {
    --stage: #2b2b2b;
    --ink: #000000;
    --pattern: #0f0f0f;
    --paper: #ffffff;
    --brand-blue: #1b8fd0;
  }
  * { box-sizing: border-box; margin: 0; padding: 0; }
  html, body { width: 1200px; height: 880px; overflow: hidden; }
  body {
    background: var(--stage);
    font-family: "Roboto", Arial, sans-serif;
    position: relative;
  }
  .card {
    position: absolute;
    left: 280px;
    width: 640px;
    height: 366px;
    border-radius: 18px;
    overflow: hidden;
  }
  .card--front { top: 50px; background: var(--ink); }
  .card--back { top: 464px; background: var(--paper); }

  .pattern-fill {
    position: absolute; inset: 0;
    background: radial-gradient(ellipse at 50% 50%, #161616 0%, var(--pattern) 70%);
  }

  .wordmark {
    position: absolute;
    font-family: "Roboto", Arial, sans-serif;
    font-weight: 700;
    font-size: 34px;
    line-height: 1.1;
    white-space: nowrap;
  }
  .card--front .wordmark {
    left: 0; right: 0; top: 160px;
    text-align: center;
    color: var(--paper);
  }
  .card--back .wordmark {
    left: 36px; top: 72px;
    color: var(--ink);
  }

  .bands { position: absolute; inset: 0; width: 640px; height: 366px; }

  .person {
    position: absolute; left: 36px; top: 202px;
    color: var(--paper);
  }
  .person__name { font-size: 23px; font-weight: 700; line-height: 1.2; }
  .person__role { font-size: 15px; margin-top: 2px; }

  .contacts {
    position: absolute; left: 36px; top: 274px;
    list-style: none;
    color: var(--paper);
    font-size: 14px;
  }
  .contacts li { display: flex; align-items: center; gap: 10px; height: 24px; }
  .contacts svg { width: 16px; height: 16px; flex: none; }

  .address {
    position: absolute; right: 30px; top: 196px;
    color: var(--paper);
    font-size: 14px;
    font-style: normal;
    text-align: right;
    line-height: 1.4;
  }
</style>
</head>
<body>
  <section class="card card--front" aria-label="Business card front">
    <div class="pattern-fill" role="img" aria-label="Dark repeating brand pattern background"></div>
    <p class="wordmark">Bright Ridge Painting LLC</p>
  </section>

  <section class="card card--back" aria-label="Business card back">
    <svg class="bands" viewBox="0 0 640 366" aria-hidden="true">
      <path d="M0 192 H270 C296 192 300 140 330 140 H640 V366 H0 Z" fill="var(--brand-blue)"/>
      <path d="M0 260 H300 C326 260 330 166 360 166 H640 V366 H0 Z" fill="var(--ink)"/>
    </svg>

    <p class="wordmark">Bright Ridge Painting LLC</p>

    <div class="person">
      <p class="person__name">Mark Delvecchi</p>
      <p class="person__role">President &amp; CEO</p>
    </div>

    <ul class="contacts">
      <li>
        <svg viewBox="0 0 16 16"><circle cx="8" cy="8" r="7.5" fill="var(--brand-blue)"/><path d="M5 4.5l1.5-.5 1 2-1 .8a5 5 0 0 0 2.7 2.7l.8-1 2 1-.5 1.5c-3.5.3-6.8-3-6.5-6.5z" fill="#fff"/></svg>
        630-584-3907
      </li>
      <li>
        <svg viewBox="0 0 16 16"><circle cx="8" cy="8" r="7.5" fill="var(--brand-blue)"/><rect x="4" y="5.5" width="8" height="5.5" fill="#fff"/><path d="M4 5.5l4 3 4-3" fill="none" stroke="var(--brand-blue)" stroke-width="0.9"/></svg>
        info@brightridgepaint.com
      </li>
      <li>
        <svg viewBox="0 0 16 16"><circle cx="8" cy="8" r="7.5" fill="var(--brand-blue)"/><circle cx="8" cy="8" r="4" fill="none" stroke="#fff" stroke-width="1"/><path d="M4 8h8M8 4c-2 2.5-2 5.5 0 8M8 4c2 2.5 2 5.5 0 8" fill="none" stroke="#fff" stroke-width="0.8"/></svg>
        www.brightridgepaint.com
      </li>
    </ul>

    <address class="address">
      PO Box 418, Elm Street<br>
      4th Lane, Naperville
    </address>
  </section>
</body>
</html>
```